Morvella! Poster

I need a poster for an event to be staged in Gibraltar called Morvella!
Morvella! is a food festival and street party that celebrates GIbraltar's multicultural and colour community. The event has a tagline "Flavours of the Open Table".
I am looking for a poster which captures the spirit of the event without being too obvious.
Updates

Because this event is rapidly approaching I would like to settle the design for the poster as soon as possible, so the earlier you post the better
thanks

I am trying to avoid a poster that looks too similar to last year's.
Red and White are Gibraltar's national colours and I would like to feature them in the design.
Morvella! the name needs to be in Clarendon! (bold) with tight character spacing

Target Market(s)

Target market are the people of Gibraltar - Gibraltar is a british colony in southern Spain, population 30,000 - Gibraltarians are of British, Spanish, Italian (Genoa), Portugese and Moroccan extraction. Gibraltar also has large Hindu, Jewish and Moroccan Communities.

Industry/Entity Type

Events

Requirements
Must have
• Initially I am looking for an A2 design - we will use the same design themes for the website and also base a 120cm x 90cm banner on the design.
• Must have t
• "BrightLanternShows.com" "Morvella!" , "Flavours of the Open Table", Friday June 19th 2009, Tollgate Plaza, Starts 21.00 hrs Finishes 0100 hrs, Free Entry, Everyone Welcome, Firework and Laser Display at 22.30 hrs
• My company logo, Office of Heritage Summer Fair Logo
• Title must use Clarendon font
Nice to have
• Could be a photo or an illustration nothing that too obviously reflects the theme, doesn''t need to have all or anymore than one of the main Gibraltarian cultures
Should not have
• picture of the ROck of Gibaltar, Money, bad photography in particular bad food photography, just a picture of some food

```html
<!DOCTYPE html>
<html lang="en">
<head>
<meta charset="utf-8">
<title>Morvella! Food Festival Street Party</title>
<link rel="stylesheet" href="https://fonts.googleapis.com/css2?family=Alfa+Slab+One&family=Alegreya:ital,wght@0,800;1,800&family=Roboto+Condensed:wght@700&family=Roboto:wght@700&display=swap">
<style>
  :root {
    --red: #ea4138;
    --blush: #fcd6cb;
    --ink: #161616;
    --paper: #ffffff;
    --buffet-white: #f3f1ee;
    --buffet-blue: #1f3d8c;
    --buffet-gold: #d99a4a;
    --buffet-green: #6f9a3a;
  }
  * { margin: 0; padding: 0; box-sizing: border-box; }
  html, body {
    width: 1200px; height: 908px; overflow: hidden;
    background: var(--paper);
  }
  .poster {
    position: relative; width: 1200px; height: 908px;
    background: var(--paper); overflow: hidden;
  }
  .top-band {
    position: absolute; left: 22px; top: 22px; width: 1160px; height: 45px;
    background: var(--red);
  }
  .side-band {
    position: absolute; left: 22px; top: 22px; width: 46px; height: 866px;
    background: var(--red);
  }
  .site-url {
    position: absolute; left: 96px; top: 38px;
    font: 700 16px/1 "Roboto", sans-serif;
    letter-spacing: 3.4px; color: var(--paper);
  }
  .food-visual {
    position: absolute; left: 710px; top: 67px; width: 472px; height: 821px;
    background:
      radial-gradient(ellipse 30% 8% at 60% 12%, rgba(217,154,74,.75), transparent 70%),
      radial-gradient(ellipse 28% 10% at 35% 30%, rgba(217,154,74,.8), transparent 70%),
      radial-gradient(ellipse 40% 12% at 75% 35%, rgba(111,154,58,.55), transparent 70%),
      radial-gradient(ellipse 30% 18% at 90% 40%, rgba(31,61,140,.55), transparent 70%),
      radial-gradient(ellipse 35% 10% at 40% 52%, rgba(200,70,60,.55), transparent 70%),
      radial-gradient(ellipse 22% 12% at 22% 72%, rgba(190,190,195,.9), transparent 70%),
      radial-gradient(ellipse 20% 10% at 40% 85%, rgba(31,61,140,.5), transparent 70%),
      linear-gradient(180deg, #f6efe6 0%, #e9e2d8 30%, var(--buffet-white) 60%, #f7f7f7 100%);
    -webkit-mask-image: linear-gradient(90deg, transparent 0%, #000 14%);
            mask-image: linear-gradient(90deg, transparent 0%, #000 14%);
  }
  .event-title {
    position: absolute; left: 90px; top: 132px;
    font: 400 118px/1 "Alfa Slab One", serif;
    letter-spacing: -2px; color: var(--red);
  }
  .kind-band {
    position: absolute; left: 68px; top: 266px; width: 678px; height: 64px;
    background: var(--red);
  }
  .kind-band span {
    position: absolute; left: 23px; top: 16px;
    font: 700 32px/1 "Roboto", sans-serif;
    letter-spacing: 1.6px; color: var(--paper);
  }
  .tagline-band {
    position: absolute; left: 22px; top: 331px; width: 724px; height: 67px;
    background: var(--blush);
  }
  .tagline-band span {
    position: absolute; left: 69px; top: 14px;
    font: 800 35px/1 "Alegreya", serif;
    letter-spacing: 1.2px; color: var(--red);
  }
  .details { position: absolute; left: 90px; top: 0; width: 620px; }
  .detail {
    position: absolute; left: 0;
    font: 700 23px/1.24 "Roboto Condensed", sans-serif;
    color: var(--ink); white-space: nowrap;
  }
  .rule {
    position: absolute; left: 0; width: 618px; height: 3px;
    background: linear-gradient(90deg, var(--red) 0%, rgba(234,65,56,.55) 55%, rgba(234,65,56,0) 100%);
  }
  .partner-mark {
    position: absolute; left: 300px; top: 770px;
    display: flex; align-items: center; gap: 8px;
  }
  .partner-mark .dot {
    width: 26px; height: 26px; border-radius: 50%; background: var(--red); flex: none;
  }
  .partner-mark span, .company-mark span {
    font: 700 17px/1.1 "Roboto Condensed", sans-serif; color: var(--ink);
  }
  .partner-mark span { width: 120px; }
  .company-mark {
    position: absolute; left: 466px; top: 812px;
    display: flex; align-items: center; gap: 8px;
  }
  .company-mark .square { width: 20px; height: 20px; background: var(--ink); flex: none; }
  .company-mark span { letter-spacing: 1.5px; }
</style>
</head>
<body>
<main class="poster">
  <div class="food-visual" role="img" aria-label="Photograph of a long buffet table laid with canapés, pastries, salads and silver platters on white and blue cloths"></div>

  <div class="top-band"></div>
  <div class="side-band"></div>
  <p class="site-url">BrightLanternShows.com</p>

  <h1 class="event-title">Morvella!</h1>
  <div class="kind-band"><span>FOOD FESTIVAL STREET PARTY</span></div>
  <div class="tagline-band"><span>Flavours of the Open Table</span></div>

  <section class="details">
    <p class="detail" style="top:440px">Friday June 19th 2009, Tollgate Plaza,<br>Starts 21.00 hrs Finishes 0100 hrs,</p>
    <div class="rule" style="top:514px"></div>
    <p class="detail" style="top:546px">Free Entry, Everyone Welcome,</p>
    <div class="rule" style="top:584px"></div>
    <p class="detail" style="top:610px">Firework and Laser Display at 22.30 hrs</p>
    <div class="rule" style="top:653px"></div>
  </section>

  <div class="partner-mark"><div class="dot"></div><span>Office of Heritage Summer Fair</span></div>
  <div class="company-mark"><div class="square"></div><span>BRIGHT LANTERN SHOWS</span></div>
</main>
</body>
</html>
```